Quill Ridge Business cards

We need business cards for our aviation company called Quill Ridge Aviation. The colour scheme is the same as the one in the logo you design (metallic green/ similar to the colours on the aircraft). The design needs to be unique and stand out.

Industry/Entity Type

Business

```html
<!DOCTYPE html>
<html lang="en">
<head>
<meta charset="utf-8">
<title>Quill Ridge Aviation – Business Cards</title>
<link href="https://fonts.googleapis.com/css2?family=Source+Sans+3:wght@400&display=swap" rel="stylesheet">
<style>
  :root {
    --page-bg: #ffffff;
    --band-green: #95c4b2;
    --mark-circle: #a7d0c4;
    --halo: rgba(214, 236, 229, 0.45);
    --ink-dark: #3b5a4a;
    --ink-light: #d9ede7;
    --backdrop-circle: #e6f1ee;
  }
  html, body {
    margin: 0;
    padding: 0;
    overflow: hidden;
    background: var(--page-bg);
  }
  .canvas {
    display: block;
    width: 1200px;
    height: 1000px;
  }
  .brand-name {
    font-family: "Source Sans 3", "Myriad Pro", sans-serif;
    font-weight: 400;
  }
  .brand-name--front { fill: var(--ink-dark); font-size: 17px; }
  .brand-name--back  { fill: var(--ink-light); font-size: 13.5px; }
  .brand-name--hero  { fill: var(--ink-dark); font-size: 44px; }
  .band { fill: var(--band-green); }
  .halo { fill: var(--halo); }
  .mark-circle { fill: var(--mark-circle); }
  .backdrop-circle { fill: var(--backdrop-circle); }
</style>
</head>
<body>
<svg class="canvas" viewBox="0 0 1200 1000" xmlns="http://www.w3.org/2000/svg">
  <defs>
    <radialGradient id="card-surface" cx="0.3" cy="0.25" r="0.95">
      <stop offset="0" stop-color="#b9c7c1"/>
      <stop offset="0.3" stop-color="#7cbcb0"/>
      <stop offset="0.65" stop-color="#3f9c90"/>
      <stop offset="1" stop-color="#2d5443"/>
    </radialGradient>
    <filter id="card-shadow" x="-5%" y="-5%" width="112%" height="115%">
      <feDropShadow dx="2" dy="3" stdDeviation="2.5" flood-color="#000" flood-opacity="0.35"/>
    </filter>
    <filter id="mark-shadow" x="-40%" y="-40%" width="200%" height="200%">
      <feDropShadow dx="5" dy="6" stdDeviation="4" flood-color="#0f2a22" flood-opacity="0.45"/>
    </filter>
    <clipPath id="front-clip"><rect x="58" y="81" width="567" height="324"/></clipPath>
    <clipPath id="back-clip"><rect x="52" y="581" width="574" height="327"/></clipPath>
  </defs>

  <!-- Brand backdrop -->
  <g class="brand-panel">
    <circle class="backdrop-circle" cx="1200" cy="500" r="493"/>
    <circle class="mark-circle" cx="1038" cy="850" r="42"/>
    <text class="brand-name brand-name--hero" x="705" y="950">Quill Ridge Aviation</text>
  </g>

  <!-- Card front -->
  <g class="card card--front">
    <rect x="58" y="81" width="567" height="324" fill="url(#card-surface)" filter="url(#card-shadow)"
          role="img" aria-label="Weathered teal paper texture"/>
    <g clip-path="url(#front-clip)">
      <path class="band" d="M58 81 H625 V92 C560 112 420 121 341 121 C262 121 120 112 58 92 Z"/>
      <path class="band" d="M58 405 H625 V394 C560 372 420 363 341 363 C262 363 120 372 58 394 Z"/>
      <circle class="halo" cx="57" cy="241" r="117"/>
    </g>
    <text class="brand-name brand-name--front" x="209" y="248">Quill Ridge Aviation</text>
    <circle class="mark-circle" cx="554" cy="241" r="27" filter="url(#mark-shadow)"/>
  </g>

  <!-- Card back -->
  <g class="card card--back">
    <rect x="52" y="581" width="574" height="327" fill="url(#card-surface)" filter="url(#card-shadow)"
          role="img" aria-label="Weathered teal paper texture"/>
    <g clip-path="url(#back-clip)">
      <circle class="halo" cx="620" cy="747" r="108"/>
    </g>
    <circle class="mark-circle" cx="86" cy="852" r="19" filter="url(#mark-shadow)"/>
    <text class="brand-name brand-name--back" x="66" y="894">Quill Ridge Aviation</text>
  </g>
</svg>
</body>
</html>
```